A new healing and spiritual podcast needs a design.

We need a design for the podcast that will also be used on the supporting website. The name is Still Lantern Path. The podcast will be about tapping into our own guidance to have a great life. There will be interviews, meditations, discussions on all aspects of energy healing and alternative healing techniques. The website will be where classes will be offered. Looking for something that conveys a peaceful feeling without looking too "healy-feely". Yet also want it to get peoples attention.

Target Market(s)

Metaphysical, spiritual (not religious), energy healers

Font styles to use
Serif

Requirements
Must have
• The name "Still Lantern Path"
Nice to have
• I'd like it to be inviting, catch peoples eye, convey a peaceful feeling, yet not be boring.
Should not have
• Animated (like comic strip) images.

```html
<!DOCTYPE html>
<html lang="en">
<head>
<meta charset="UTF-8">
<title>Still Lantern Path — Podcast Cover</title>
<link rel="stylesheet" href="https://fonts.googleapis.com/css2?family=Cormorant+Garamond:wght@500;700&display=swap">
<style>
  :root {
    --sky-top: #8d5c96;
    --sky-mid: #7c4987;
    --haze: #9b6aa4;
    --ridge: #55295c;
    --rock: #3a1a40;
    --ground: #24102a;
    --glow: rgba(240, 214, 246, 0.55);
    --ink-light: #ffffff;
    --arc-violet: rgba(172, 112, 184, 0.85);
  }
  * { margin: 0; padding: 0; box-sizing: border-box; }
  html, body {
    width: 1200px;
    height: 1200px;
    overflow: hidden;
    background: var(--ground);
  }
  .cover {
    position: relative;
    width: 1200px;
    height: 1200px;
    overflow: hidden;
    font-family: "Cormorant Garamond", "Garamond", serif;
  }
  .cover__scene {
    position: absolute;
    inset: 0;
    background:
      radial-gradient(circle at 850px 500px, var(--glow) 0, rgba(240, 214, 246, 0.18) 90px, rgba(240, 214, 246, 0) 220px),
      linear-gradient(160deg, rgba(0, 0, 0, 0) 40%, rgba(36, 16, 42, 0.35) 100%),
      linear-gradient(180deg,
        var(--sky-top) 0%,
        var(--sky-mid) 38%,
        var(--haze) 52%,
        var(--ridge) 66%,
        var(--rock) 82%,
        var(--ground) 100%);
  }
  .cover__arcs {
    position: absolute;
    inset: 0;
    width: 1200px;
    height: 1200px;
  }
  .title-block {
    position: absolute;
    left: 82px;
    top: 414px;
    color: var(--ink-light);
  }
  .title-block__rule {
    width: 152px;
    height: 11px;
    background: var(--ink-light);
    margin-bottom: 58px;
  }
  .title-block__line {
    display: block;
    font-size: 104px;
    line-height: 112px;
  }
  .title-block__line--light {
    font-weight: 500;
    letter-spacing: 1px;
  }
  .title-block__line--strong {
    font-weight: 700;
    text-transform: uppercase;
    letter-spacing: 4px;
  }
</style>
</head>
<body>
  <main class="cover">
    <div class="cover__scene" role="img" aria-label="Photograph: a person seen from behind meditating cross-legged on a rocky mountain summit, sunlight glowing beside them, misty ridges beneath a violet sky"></div>

    <svg class="cover__arcs" viewBox="0 0 1200 1200" aria-hidden="true">
      <defs>
        <linearGradient id="arc-fade" x1="0" y1="118" x2="0" y2="1032" gradientUnits="userSpaceOnUse">
          <stop offset="0" stop-color="#ecd6f0" stop-opacity="0.7"/>
          <stop offset="0.55" stop-color="#dcbce3" stop-opacity="0.6"/>
          <stop offset="1" stop-color="#b07cbc" stop-opacity="0.75"/>
        </linearGradient>
      </defs>
      <path class="arc arc--outer" d="M686 124 A451 451 0 0 1 686 1026"
            fill="none" stroke="url(#arc-fade)" stroke-width="14"/>
      <path class="arc arc--inner" d="M1092 612 A400 400 0 0 1 686 988"
            fill="none" stroke="var(--arc-violet)" stroke-width="14"/>
    </svg>

    <header class="title-block">
      <div class="title-block__rule"></div>
      <h1>
        <span class="title-block__line title-block__line--light">Still Lantern</span>
        <span class="title-block__line title-block__line--strong">Path</span>
      </h1>
    </header>
  </main>
</body>
</html>
```